Restaurant service company needs a website!

I am looking for a skilled web designer/developer to create a professional, responsive, and easy-to-navigate website for my company, which specializes in servicing restaurant cooking equipment. The site should communicate trust, reliability, and technical expertise to our target audience, restaurant owners, managers, and commercial kitchen operators. I have included the company logos, if any other format for them is needed please let me know.

Target Market(s)

restaurant owners, managers, and commercial kitchen operators

Industry/Entity Type

Commercial Kitchen Equipment Service

Coding

Coded - Design and coding required

Number of Pages Required

1 page

Font styles to use
Serif
Sans Serif

Requirements
Must have
• Contact and service request forms, Click-to-call functionality for mobile, Clean, modern layout with strong visuals, Easy navigation, mobile-friendly
Nice to have
• Testimonials or Reviews, If possible a click-to-text functionality for mobile.
Should not have
• Any mention of Refrigeration or HVAC, "Free Quotes"

```html
<!DOCTYPE html>
<html lang="en">
<head>
<meta charset="utf-8">
<title>Kitchenline Restaurant Service</title>
<link href="https://fonts.googleapis.com/css2?family=Montserrat:wght@400;500;600;700&display=swap" rel="stylesheet">
<style>
:root{
  --backdrop:#cfcfd1;
  --teal:#0e6480;
  --teal-dark:#0b4f66;
  --ink:#1e1e1e;
  --muted:#555;
  --pale-blue:#cfe0e6;
  --pale-gray:#e5ebf0;
  --field:#e9eef2;
  --white:#fff;
  --charcoal:#232528;
}
*{box-sizing:border-box;margin:0;padding:0}
html,body{width:1200px;height:4686px;overflow:hidden}
body{background:var(--backdrop);font-family:'Montserrat',sans-serif;color:var(--ink)}
.page{position:absolute;left:155px;top:144px;width:909px;background:var(--white)}
section,header,footer{position:relative;width:909px}
.abs{position:absolute}
.tool{position:absolute;left:268px;width:378px;height:46px;z-index:5}
.badge{position:absolute;left:392px;top:89px;width:128px;height:128px;border-radius:50%;background:radial-gradient(circle,#e0a530 0 45%,#2a2a2a 46% 100%);z-index:6}

/* header */
.site-header{height:153px}
.brand{left:71px;top:50px;display:flex;align-items:center;gap:8px}
.brand-mark{width:22px;height:22px;border:2px solid var(--teal)}
.brand-name{font-size:20px;font-weight:700;color:var(--teal);letter-spacing:.5px}
.phone{right:90px;top:32px;font-size:13px;display:flex;gap:8px;align-items:center}
.phone span.dot{width:14px;height:14px;border-radius:50%;background:#3bb54a}
.nav{right:90px;top:62px;display:flex;gap:22px;font-size:10px;font-weight:500}

/* hero */
.hero{height:533px}
.hero-photo{left:0;top:0;width:909px;height:295px;background:linear-gradient(180deg,#4a4c4f,#8a8d90 60%,#6b6e71)}
.hero-title{left:0;top:140px;width:909px;text-align:center;color:#fff;font-size:23px;font-weight:600;line-height:29px}
.features{left:71px;top:295px;width:771px;height:182px;display:flex}
.feature{flex:1;padding:30px 14px 0;text-align:center}
.feature.dark{background:var(--teal);color:#fff}
.feature.light{background:var(--pale-blue);color:var(--ink)}
.feature svg{width:30px;height:30px}
.feature h3{font-size:15px;font-weight:600;margin:12px 0 8px}
.feature p{font-size:8px;line-height:11px}

/* satisfaction */
.satisfaction{height:507px;background:var(--pale-blue)}
.sat-card{left:71px;top:67px;width:771px;height:375px;background:#fff;display:flex}
.sat-photo{width:314px;height:375px;background:linear-gradient(160deg,#bfc4c7,#7d8387 60%,#5c6266)}
.sat-body{padding:34px 40px 0 42px;flex:1}
.sat-body h2{font-size:19px;font-weight:700;margin-bottom:14px}
.sat-body>p{font-size:9px;line-height:11px;margin-bottom:18px}
.sat-item{display:flex;gap:14px;margin-bottom:18px}
.sat-item .ic{width:18px;height:18px;flex:none}
.sat-item h4{font-size:12px;font-weight:600;margin-bottom:8px}
.sat-item p{font-size:8.5px;line-height:11px}

/* why */
.why{height:482px}
.why h2{position:absolute;top:114px;width:909px;text-align:center;font-size:31px;font-weight:500}
.why-left{left:87px;top:200px;width:330px}
.why-left h4{font-size:15px;font-weight:600;margin-bottom:26px}
.why-left p{font-size:14px;line-height:18px;padding-left:20px}
.why-right{left:467px;top:200px;list-style:none}
.why-right li{font-size:16px;font-weight:600;margin-bottom:20px}
.why-right li::before{content:"+";margin-right:10px}

/* showcase */
.showcase{height:709px;background:linear-gradient(90deg,var(--teal) 0%,#0d4a5e 55%,var(--charcoal) 100%);color:#fff}
.showcase h2{position:absolute;top:60px;width:909px;text-align:center;font-size:24px;font-weight:600;line-height:29px}
.showcase .lead{position:absolute;top:136px;width:909px;text-align:center;font-size:10px;line-height:12px}
.shot{background:linear-gradient(150deg,#d8dcdf,#8c9297)}
.btn-pair{left:358px;top:610px;display:flex;border:2px solid #fff;border-radius:14px;overflow:hidden}
.btn-pair span{font-size:10px;padding:6px 20px}
.btn-pair .on{background:var(--teal)}
.btn-pair .off{background:#fff;color:var(--ink)}

/* testimonials */
.reviews{height:391px}
.reviews h2{position:absolute;top:48px;width:909px;text-align:center;font-size:31px;font-weight:500}
.quote{top:127px;width:245px;height:151px;background:var(--teal);color:#fff;padding:22px 24px;font-size:11px;line-height:17px}
.quote .stars{font-size:17px;letter-spacing:2px;margin-top:4px}
.arrow{top:190px;color:#fff;font-size:20px}
.person{top:300px;display:flex;gap:12px;align-items:center}
.person .av{width:34px;height:34px;border-radius:50%;background:#d4b08f}
.person b{display:block;font-size:14px;font-weight:500}
.person small{font-size:9px;color:#888}

/* process */
.process{height:500px;background:var(--pale-gray)}
.pill{left:416px;top:48px;background:var(--teal);color:#fff;font-size:9px;padding:3px 10px;border-radius:10px}
.process h2{position:absolute;top:80px;width:909px;text-align:center;font-size:24px;font-weight:600;line-height:30px}
.process .lead{position:absolute;top:148px;width:909px;text-align:center;font-size:10px;line-height:12px}
.steps{left:71px;top:196px;width:771px;height:180px;display:flex}
.step{flex:1;text-align:center;padding-top:32px}
.step.dark{background:var(--teal);color:#fff}
.step svg{width:34px;height:34px}
.step h4{font-size:12px;font-weight:500;margin:20px 0 8px}
.step p{font-size:7px;line-height:10px;padding:0 22px}

/* contact */
.contact{height:833px}
.contact .tag{position:absolute;top:10px;width:909px;text-align:center;font-size:31px;font-weight:500}
.contact h2{position:absolute;left:71px;top:86px;font-size:31px;font-weight:500}
.lbl{font-size:7px;font-weight:600;position:absolute;left:71px}
.fld{position:absolute;left:74px;width:355px;height:32px;background:var(--field);font-size:11px;color:#999;padding:8px 14px}
.send{left:74px;top:650px;width:355px;height:20px;background:var(--teal);color:#fff;font-size:8px;text-align:center;line-height:20px}
.map{left:71px;top:675px;width:358px;height:356px;background:linear-gradient(135deg,#e8ece9,#d8e2dc 50%,#c8d7e2)}
.booking{left:458px;top:95px;width:384px;height:691px;background:var(--pale-gray);padding:28px 20px}
.booking h3{text-align:center;font-size:16px;font-weight:600}
.booking .note{text-align:center;font-size:8px;margin:12px 0 32px;line-height:14px}
.bk-sec{font-size:7px;color:var(--teal);font-weight:600;margin:12px 0 6px}
.bk-row{display:flex;gap:10px;margin-bottom:4px}
.bk-row div{flex:1}
.bk-row label{display:block;font-size:6.5px;margin-bottom:3px}
.bk-row i{display:block;height:16px;background:#fff;font-style:normal;font-size:6.5px;padding:3px 6px}
.bk-area{height:44px;background:#fff;margin-bottom:6px}
.bk-btn{background:var(--teal);color:#fff;font-size:7px;text-align:center;height:18px;line-height:18px;margin:8px 0}
.bk-small{font-size:5.5px}

/* footer */
.site-footer{height:231px;background:var(--teal);color:#fff}
.f-logo{left:71px;top:52px;width:50px;height:58px;border:2px solid #fff;font-size:6px;text-align:center;padding-top:38px;font-weight:700}
.f-col h5{font-size:9px;font-weight:600;margin-bottom:12px}
.f-col p{font-size:8px;margin-bottom:9px}
.f-btn{background:#fff;color:var(--teal);font-size:8px;border-radius:10px;text-align:center;padding:5px 0;width:132px;margin-top:10px}
.socials{left:496px;top:152px;display:flex;gap:8px}
.socials span{width:20px;height:20px;border-radius:50%;background:#fff}
.f-badge{left:490px;top:50px;width:92px;height:92px;border-radius:50%;background:radial-gradient(circle,#e0a530 0 45%,#2a2a2a 46% 100%)}
.insta{left:655px;top:76px;display:grid;grid-template-columns:repeat(3,58px);gap:6px}
.insta span{height:58px;background:linear-gradient(150deg,#d6dadd,#7c8387)}
.bottom-bar{height:40px;font-size:7px;display:flex;align-items:center;padding:0 71px;gap:28px}
.bottom-bar .right{margin-left:auto}
</style>
</head>
<body>
<div class="page">

  <header class="site-header">
    <div class="abs brand"><span class="brand-mark"></span><span class="brand-name">KITCHENLINE</span></div>
    <div class="abs phone"><span class="dot"></span>
      <svg width="14" height="14" viewBox="0 0 24 24"><path d="M6 2l4 4-2 3a12 12 0 006 6l3-2 4 4-3 4C9 20 4 15 2 5z" fill="#1e1e1e"/></svg>
      | 800-555-0142</div>
    <nav class="abs nav"><span>Home</span><span>About Us</span><span>Our Service</span><span>Book Service</span><span>Contact Us</span></nav>
  </header>
  <div class="badge" role="img" aria-label="Satisfaction guaranteed seal"></div>

  <section class="hero">
    <div class="abs hero-photo" role="img" aria-label="Chefs working in a commercial kitchen"></div>
    <h1 class="abs hero-title">Reliable and Experienced<br>Restauranr Equipment Maintenance Team</h1>
    <div class="abs features">
      <div class="feature dark">
        <svg viewBox="0 0 24 24"><circle cx="12" cy="9" r="6" fill="#fff"/><path d="M8 14l-2 8 6-3 6 3-2-8z" fill="#fff"/></svg>
        <h3>Certified</h3><p>Our certified technicians can diagnose and repair all major commercial brands</p></div>
      <div class="feature light">
        <svg viewBox="0 0 24 24"><circle cx="10" cy="7" r="4" fill="#333"/><path d="M2 22a8 8 0 0116 0z" fill="#333"/></svg>
        <h3>Trusted</h3><p>We're dedicated to serving our community with top-notch equipment care</p></div>
      <div class="feature dark">
        <svg viewBox="0 0 24 24"><path d="M12 22V12M12 12C12 6 6 4 3 4c0 4 3 8 9 8zm0 0c0-6 6-8 9-8 0 4-3 8-9 8z" stroke="#fff" stroke-width="2" fill="#fff"/></svg>
        <h3>Transparent Pricing</h3><p>No hidden fees or surprises. We provide upfront estimates before starting work.</p></div>
      <div class="feature light">
        <svg viewBox="0 0 24 24"><circle cx="12" cy="12" r="10" fill="#222"/><path d="M12 6v6l4 3" stroke="#fff" stroke-width="2" fill="none"/></svg>
        <h3>Prompt Service</h3><p>We understand your time is valuable, so we offer same-day or next-day appointments.</p></div>
    </div>
    <div class="tool" style="top:460px" role="img" aria-label="Screwdriver illustration">
      <svg width="378" height="46"><rect x="0" y="21" width="200" height="4" fill="#666"/><rect x="200" y="6" width="178" height="34" rx="17" fill="#1b2430"/></svg></div>
  </section>

  <section class="satisfaction">
    <div class="abs sat-card">
      <div class="sat-photo" role="img" aria-label="Chef in a stainless steel kitchen"></div>
      <div class="sat-body">
        <h2>Customer Satisfaction Guaranteed</h2>
        <p>Our goal is to provide the highest level of service and ensure your complete satisfaction. We pride ourselves on our professionalism, attention to detail, and commitment to customer care. From the moment you contact us to the completion of your service/repair, we're dedicated to making the process as smooth and stress-free as possibl</p>
        <div class="sat-item"><svg class="ic" viewBox="0 0 24 24"><circle cx="12" cy="12" r="8" stroke="#222" stroke-width="3" fill="none"/><path d="M12 2v20M2 12h20" stroke="#222" stroke-width="2"/></svg>
          <div><h4>Extensive Brand Coverage</h4><p>We are able to provide services for a diverse assortment of brands, ranging from high-end luxury to everyday household names.</p></div></div>
        <div class="sat-item"><svg class="ic" viewBox="0 0 24 24"><circle cx="7" cy="5" r="3" fill="#222"/><circle cx="17" cy="5" r="3" fill="#222"/><rect x="4" y="9" width="6" height="12" fill="#222"/><rect x="14" y="9" width="6" height="12" fill="#222"/></svg>
          <div><h4>Brand-Specific Training</h4><p>In order to maintain a current knowledge of most recent brand technologies, our team participates in ongoing training</p></div></div>
        <div class="sat-item"><svg class="ic" viewBox="0 0 24 24"><circle cx="12" cy="12" r="10" fill="#222"/></svg>
          <div><h4>Warrant Compliance</h4><p>All of our repairs are guaranteed to be in accordance with the manufacturer's warranty, thereby preserving your coverage.</p></div></div>
      </div>
    </div>
    <div class="tool" style="top:478px" role="img" aria-label="Screwdriver illustration">
      <svg width="378" height="46"><rect x="0" y="21" width="200" height="4" fill="#666"/><rect x="200" y="6" width="178" height="34" rx="17" fill="#1b2430"/></svg></div>
  </section>

  <section class="why">
    <h2>Why Service your Equipment?</h2>
    <div class="abs why-left">
      <h4>-&nbsp;&nbsp; Operational Efficiency</h4>
      <p>Well-maintained equipment operates smoothly, allowing for faster service and consistent food quality. For instance, a properly calibrated oven ensures even cooking and can significantly reduce preparation times. In contrast, neglected equipment can lead to delays and inconsistencies, frustrating both staff and customers.</p>
    </div>
    <ul class="abs why-right">
      <li>Food Safety</li><li>Cost Savings</li><li>Avoiding Breakdowns</li><li>Compliance with Health Regulations</li>
    </ul>
  </section>

  <section class="showcase">
    <h2>Our Featured Showcase of<br>Successful Projects</h2>
    <p class="lead">Discover how Kitchenline has helped countless Restaurants<br>with their equipment service needs.<br>Browse through our recent projects to see the quality and expertise that define our services.</p>
    <div class="abs shot" style="left:71px;top:204px;width:373px;height:371px" role="img" aria-label="Chefs cooking in a serviced kitchen"></div>
    <div class="abs shot" style="left:465px;top:204px;width:377px;height:180px" role="img" aria-label="Chef at a kitchen workstation"></div>
    <div class="abs shot" style="left:465px;top:399px;width:377px;height:176px" role="img" aria-label="Clean stainless steel kitchen line"></div>
    <div class="abs btn-pair"><span class="on">Book Service</span><span class="off">View all Projects</span></div>
  </section>

  <section class="reviews">
    <h2>Satisfied Customers</h2>
    <div class="abs quote" style="left:71px">Lorem ipsum dolor sit amet, sed diam adipiscing elit, sed diam nonummy nibh euismod tincidunt ut laoreet dolore magna aliquam erat volutpat. Ut wisi enim ad tincidunt ut laoreet dolore<div class="stars">★★★★★</div></div>
    <div class="abs quote" style="left:333px">Lorem ipsum dolor sit amet, sed diam adipiscing elit, sed diam nonummy nibh euismod tincidunt ut laoreet dolore magna aliquam erat volutpat. Ut wisi enim ad tincidunt ut laoreet dolore<div class="stars">★★★★★</div></div>
    <div class="abs quote" style="left:595px">Lorem ipsum dolor sit amet, sed diam adipiscing elit, sed diam nonummy nibh euismod tincidunt ut laoreet dolore magna aliquam erat volutpat. Ut wisi enim ad tincidunt ut laoreet dolore<div class="stars">★★★★★</div></div>
    <span class="abs arrow" style="left:76px">‹</span><span class="abs arrow" style="left:826px">›</span>
    <div class="abs person" style="left:71px"><span class="av" role="img" aria-label="Customer portrait"></span><div><b>Daniel Moreau</b><small>Co-Founder</small></div></div>
    <div class="abs person" style="left:333px"><span class="av" role="img" aria-label="Customer portrait"></span><div><b>Helena Brooks</b><small>Manager</small></div></div>
    <div class="abs person" style="left:595px"><span class="av" role="img" aria-label="Customer portrait"></span><div><b>Priya Nolan</b><small>Owner</small></div></div>
  </section>

  <section class="process">
    <span class="abs pill">Our Process</span>
    <h2>From Booking to Service, Our Process is<br>Simple and Seamless</h2>
    <p class="lead">Service with our simple and efficient process. We guarantee top-notch service from start to finish,<br>ensuring your appliances are in working order with minimal disruption</p>
    <div class="abs steps">
      <div class="step dark"><svg viewBox="0 0 24 24"><path d="M4 20l3-9 8-8 6 6-8 8z" fill="none" stroke="#fff" stroke-width="2"/></svg>
        <h4>Fill the Form</h4><p>Provide us with your equipment details and service needs quickly through our easy booking form</p></div>
      <div class="step"><svg viewBox="0 0 24 24"><rect x="4" y="2" width="16" height="20" fill="var(--teal)"/><rect x="7" y="5" width="10" height="4" fill="#fff"/></svg>
        <h4>Get Estimate</h4><p>Receive a transparent and accurate estimate for your equipment service, with no hidden fees</p></div>
      <div class="step dark"><svg viewBox="0 0 24 24"><rect x="3" y="4" width="18" height="17" fill="#fff"/><path d="M8 13l3 3 5-6" stroke="var(--teal)" stroke-width="2" fill="none"/></svg>
        <h4>Pick Service Time</h4><p>Choose a convenient time for your service that fits your busy schedule effortlessly</p></div>
      <div class="step"><svg viewBox="0 0 24 24"><circle cx="10" cy="7" r="4" fill="var(--teal)"/><path d="M2 21a8 8 0 0116 0z" fill="var(--teal)"/></svg>
        <h4>Service begins</h4><p>Our certified technician arrives on time ready to fix your equipment efficiently and professionally</p></div>
    </div>
    <div class="tool" style="top:426px" role="img" aria-label="Screwdriver illustration">
      <svg width="378" height="46"><rect x="0" y="21" width="200" height="4" fill="#666"/><rect x="200" y="6" width="178" height="34" rx="17" fill="#1b2430"/></svg></div>
  </section>

  <section class="contact">
    <p class="tag">One Call Fixes All</p>
    <h2>Contact Us</h2>
    <span class="lbl" style="top:165px">Name</span><div class="fld" style="top:175px">Name</div>
    <span class="lbl" style="top:222px">Email</span><div class="fld" style="top:232px">Email</div>
    <span class="lbl" style="top:279px">Message</span><div class="fld" style="top:289px;height:78px">Message</div>
    <div class="abs send" style="top:385px">Send</div>
    <div class="abs map" style="top:431px" role="img" aria-label="Map showing the office location"></div>
    <div class="abs booking">
      <h3>Book Your Maintenance Service</h3>
      <p class="note">For any queries or pre-service questions, please call us on<br><b>(123)456 7890</b></p>
      <div class="bk-sec">Service Details</div>
      <div class="bk-row"><div><label>Type of Equipment</label><i>Espresso Machine</i></div><div><label>Brand</label><i></i></div><div><label>Model Number</label><i></i></div></div>
      <div class="bk-row"><div><label>Problem Description/Issue</label></div></div><div class="bk-area"></div>
      <div class="bk-sec">Appointment Preferences</div>
      <div class="bk-row"><div><label>Preferred Service Date</label><i></i></div><div><label>Preferred Service Time</label><i></i></div></div>
      <div class="bk-sec">Urgency Level</div>
      <div class="bk-row"><div><i>Emergency</i></div><div><label>Service Frequency</label><i>One Time Service</i></div></div>
      <div class="bk-row"><div><label>Street Address</label><i></i></div></div>
      <div class="bk-row"><div><label>City</label><i></i></div><div><label>State</label><i></i></div><div><label>ZIP Code</label><i></i></div></div>
      <div class="bk-sec">Personal Information</div>
      <div class="bk-row"><div><label>First Name</label><i></i></div><div><label>Last Name</label><i></i></div></div>
      <div class="bk-row"><div><label>Phone Number</label><i></i></div><div><label>Email Address</label><i></i></div><div><label>Preferred Contact Method</label><i>Phone · Email · SMS</i></div></div>
      <div class="bk-sec">Confirmation</div>
      <p class="bk-small">I agree to the Terms and Conditions, and Privacy Policy</p>
      <div class="bk-btn">Schedule Your Booking</div>
      <p class="bk-small">Your information is strictly confidential and is used to give a smooth and efficient service experience.</p>
    </div>
  </section>

  <footer class="site-footer">
    <div class="abs f-logo">KITCHENLINE</div>
    <div class="abs f-col" style="left:150px;top:52px"><h5>Contact Info</h5><p>⌖ Street, City, Country</p><p>✆ (123) 456 7890</p><p>✉ info@company.com</p><div class="f-btn">Book Service</div></div>
    <div class="abs f-col" style="left:332px;top:52px"><h5>Information</h5><p>› About Us</p><p>› Our Service</p><p>› Reviews</p><p>› Projects</p><p>› Contact Us</p></div>
    <div class="abs f-badge" role="img" aria-label="Satisfaction guaranteed seal"></div>
    <div class="abs socials"><span></span><span></span><span></span></div>
    <div class="abs f-col" style="left:655px;top:52px"><h5>Instagram</h5></div>
    <div class="abs insta" role="img" aria-label="Kitchen project photo grid"><span></span><span></span><span></span><span></span><span></span><span></span></div>
  </footer>
  <div class="bottom-bar"><span>Terms of Use</span><span>Privacy Policy</span><span class="right">© 2025 Kitchenline. All rights reserved</span></div>

</div>
</body>
</html>
```